Content developers BC and Stationary
Nubra نبراس
Content developers BC and Stationary - Corporate Services
Creative Brief
Simple
Rana T alMuttairi
Creative Director
Jeddah
rana@nubraco.com
for second partner, with Arabic on the back: Khaled Naji خالد ناجي Managing Director المدير التنفيذي +966507213690 +٩٦٦٥٠٧٢١٣٦٩٠ k@nubraco.com
رنا طارق المطيري المدير الإبداعي +٩٦٦٥٠٨٤٤١٢٥٩ rana@nubraco.com
Concepts
Business Cards and Stationery for new compliance company.
Business Cards and Stationery for Background Check Company

```html
<!DOCTYPE html>
<html lang="en">
<head>
<meta charset="utf-8">
<title>Nubra business card</title>
<link rel="stylesheet" href="https://fonts.googleapis.com/css2?family=Tajawal:wght@400;500;700&display=swap">
<style>
  :root {
    --backdrop: #eceef0;
    --card: #ffffff;
    --purple: #7a4ea6;
    --lavender: #b79bd8;
    --lilac: #d9c8ec;
    --navy: #343c8c;
    --ink: #5a4a6e;
  }
  * { margin: 0; padding: 0; box-sizing: border-box; }
  html, body {
    width: 1200px; height: 939px; overflow: hidden;
    background: var(--backdrop);
    font-family: "Tajawal", sans-serif;
  }
  .sheet {
    position: relative; width: 1200px; height: 939px;
    display: flex; align-items: center; justify-content: center; gap: 60px;
  }
  .card {
    position: relative; width: 510px; height: 292px;
    background: var(--card);
    box-shadow: 0 6px 22px rgba(40, 40, 70, 0.12);
    overflow: hidden;
  }
  .brand {
    display: flex; align-items: center; gap: 10px;
    color: var(--purple); font-weight: 700; line-height: 1;
  }
  .brand-dot { width: 12px; height: 12px; border-radius: 50%; background: var(--purple); }

  /* contact side */
  .card-back .brand { position: absolute; left: 30px; top: 30px; font-size: 40px; }
  .address {
    position: absolute; left: 32px; top: 90px;
    font-size: 11px; line-height: 1.45; color: var(--ink);
  }
  .waves { position: absolute; left: 0; bottom: 0; width: 510px; height: 150px; }
  .person {
    position: absolute; right: 30px; top: 96px; text-align: right;
  }
  .person-name { font-size: 17px; font-weight: 500; color: var(--purple); }
  .person-role { font-size: 13px; color: var(--purple); margin-top: 2px; }
  .contacts {
    position: absolute; right: 30px; top: 152px; list-style: none;
    text-align: right; font-size: 11.5px; line-height: 1.55; color: var(--ink);
  }
  .contacts li { display: flex; justify-content: flex-end; align-items: center; gap: 6px; }
  .contacts svg { width: 10px; height: 10px; fill: var(--purple); }
  .website {
    position: absolute; right: 30px; bottom: 72px;
    font-size: 12px; color: var(--purple); letter-spacing: 0.3px;
  }

  /* logo side */
  .card-front { display: flex; align-items: center; justify-content: center; }
  .card-front .brand { font-size: 64px; gap: 16px; }
  .card-front .brand-dot { width: 18px; height: 18px; }
</style>
</head>
<body>
<main class="sheet">
  <section class="card card-back" aria-label="Business card, contact side">
    <div class="brand"><span class="brand-dot"></span><span>Nubra نبراس</span></div>
    <p class="address">12 King Road,<br>Al Rawdah District<br>Jeddah KSA</p>

    <svg class="waves" viewBox="0 0 510 150" preserveAspectRatio="none" aria-hidden="true">
      <path d="M0 40 C140 110 320 120 510 70 L510 150 L0 150 Z" fill="var(--lilac)"/>
      <path d="M0 70 C150 130 330 135 510 95 L510 150 L0 150 Z" fill="var(--lavender)"/>
      <path d="M0 62 C150 122 330 128 510 86" fill="none" stroke="var(--navy)" stroke-width="3"/>
      <path d="M0 100 C160 150 340 150 510 118 L510 150 L0 150 Z" fill="var(--purple)"/>
    </svg>

    <div class="person">
      <p class="person-name">Rana T alMuttairi</p>
      <p class="person-role">Creative Director</p>
    </div>
    <ul class="contacts">
      <li>+966 508 441 259
        <svg viewBox="0 0 10 10"><path d="M2 0.5 L4 2.5 L3 3.8 Q4.2 6 6.2 7 L7.5 6 L9.5 8 L8 9.5 Q3 9 0.5 2 Z"/></svg></li>
      <li>+966 507 213 690
        <svg viewBox="0 0 10 10"><rect x="2.5" y="0.5" width="5" height="9" rx="1"/></svg></li>
      <li>rana@nubraco.com
        <svg viewBox="0 0 10 10"><path d="M0.5 2 H9.5 V8.5 H0.5 Z M0.5 2 L5 5.5 L9.5 2" /></svg></li>
    </ul>
    <p class="website">www.nubraco.com</p>
  </section>

  <section class="card card-front" aria-label="Business card, logo side">
    <div class="brand"><span class="brand-dot"></span><span>Nubra نبراس</span></div>
  </section>
</main>
</body>
</html>
```